VELRO - Business cards

Business card to be created for Commercial sales staff

Target Market(s)

Commercial businesses

Industry/Entity Type

Commercial

Contact Information for Business Card

Look professional. For commercial clients

Colors
ffffff

Requirements
Must have
• - Velro Logo
• - Commercial sales staff as postion
• - room for commerical sales manager role
• - person name and their mobile number
• - Website : velropower.com.au
Nice to have
• White background.
• On back of business card just have the logo no other information
Should not have
• Should only have white background on front of card.

```html
<!DOCTYPE html>
<html lang="en">
<head>
<meta charset="UTF-8">
<title>Velro – Business Cards</title>
<link href="https://fonts.googleapis.com/css2?family=Montserrat:wght@400;500;600;700;800&display=swap" rel="stylesheet">
<style>
  :root {
    --stage: #e6e6e8;
    --card-dark: #2f3139;
    --card-light: #ffffff;
    --brand-red: #c8202f;
    --ink: #2f3139;
    --text-grey: #4a4c53;
    --divider: #b9bbc0;
  }
  * { margin: 0; padding: 0; box-sizing: border-box; }
  html, body {
    width: 1200px; height: 900px; overflow: hidden;
    background: var(--stage);
    font-family: "Montserrat", sans-serif;
  }
  .stage {
    position: relative; width: 1200px; height: 900px;
  }
  .card {
    position: absolute;
    width: 630px; height: 360px;
    border-radius: 22px;
    box-shadow: 0 10px 28px rgba(0,0,0,0.18);
    overflow: hidden;
  }
  /* Back of card */
  .card-back {
    left: 120px; top: 70px;
    background: var(--card-dark);
    color: #fff;
  }
  .card-back .back-logo {
    position: absolute; left: 0; right: 0; top: 120px;
    display: flex; justify-content: center; align-items: center; gap: 18px;
  }
  .back-logo .mark-dot {
    width: 34px; height: 34px; border-radius: 50%; background: #fff;
  }
  .back-logo .wordmark {
    font-weight: 800; font-size: 64px; letter-spacing: 2px; color: #fff;
  }
  .card-back .back-url {
    position: absolute; left: 0; right: 0; bottom: 36px;
    text-align: center; font-size: 17px; font-weight: 400; color: #e8e8ea;
  }
  .back-url strong { font-weight: 600; }

  /* Front of card */
  .card-front {
    left: 450px; top: 470px;
    background: var(--card-light);
  }
  .front-logo {
    position: absolute; left: 50px; top: 150px;
    display: flex; align-items: center; gap: 14px;
  }
  .front-logo .mark-dot {
    width: 30px; height: 30px; border-radius: 50%; background: var(--brand-red);
  }
  .front-logo .wordmark {
    font-weight: 800; font-size: 54px; letter-spacing: 1px; color: var(--ink);
  }
  .divider {
    position: absolute; left: 318px; top: 70px;
    width: 1.5px; height: 220px; background: var(--divider);
  }
  .details {
    position: absolute; left: 342px; top: 96px; right: 20px;
  }
  .person-name {
    font-weight: 600; font-size: 25px; color: var(--brand-red);
    letter-spacing: 0.5px; white-space: nowrap;
  }
  .role {
    font-size: 15px; color: var(--text-grey); line-height: 1.35;
  }
  .contact-list {
    list-style: none; margin-top: 14px;
  }
  .contact-list li {
    display: flex; align-items: center; gap: 10px;
    font-size: 15px; color: var(--text-grey); line-height: 1.5;
    white-space: nowrap;
  }
  .contact-list svg { width: 12px; height: 12px; flex: none; }
  .contact-list .accent { color: var(--brand-red); font-weight: 600; }
</style>
</head>
<body>
<main class="stage">
  <section class="card card-back" aria-label="Business card back">
    <div class="back-logo">
      <span class="mark-dot"></span>
      <span class="wordmark">VELRO</span>
    </div>
    <p class="back-url">www.<strong>velropower</strong>.com.au</p>
  </section>

  <section class="card card-front" aria-label="Business card front">
    <div class="front-logo">
      <span class="mark-dot"></span>
      <span class="wordmark">VELRO</span>
    </div>
    <div class="divider"></div>
    <div class="details">
      <h1 class="person-name">MARLO PRENTISS</h1>
      <p class="role">Commercial sales staff</p>
      <p class="role">Commerical sales manager</p>
      <ul class="contact-list">
        <li>
          <svg viewBox="0 0 24 24" fill="var(--brand-red)"><path d="M6.6 10.8a15.1 15.1 0 0 0 6.6 6.6l2.2-2.2c.3-.3.7-.4 1-.2 1.1.4 2.3.6 3.6.6.6 0 1 .4 1 1V20c0 .6-.4 1-1 1A17 17 0 0 1 3 4c0-.6.4-1 1-1h3.5c.6 0 1 .4 1 1 0 1.3.2 2.5.6 3.6.1.3 0 .7-.2 1z"/></svg>
          +330 2418-7093
        </li>
        <li>
          <svg viewBox="0 0 24 24" fill="none" stroke="var(--brand-red)" stroke-width="2.4"><rect x="2" y="5" width="20" height="14" rx="2"/><path d="M2 6l10 7 10-7"/></svg>
          info@velropower.com.au
        </li>
        <li>
          <svg viewBox="0 0 24 24" fill="none" stroke="var(--brand-red)" stroke-width="2.2"><circle cx="12" cy="12" r="10"/><path d="M2 12h20M12 2c3 3 3 17 0 20M12 2c-3 3-3 17 0 20"/></svg>
          www.<span class="accent">velropower</span>.com.au
        </li>
      </ul>
    </div>
  </section>
</main>
</body>
</html>
```